Stationary for Automotive Paintless Dent Repair Company
Panel Soothe LLC
Stationary for Automotive Paintless Dent Repair Company - Automotive
Creative Brief
Modern
Mark Fenley
Owner
478 Birch Ln Allentown, PA 18117
info@PanelSootheLLC.com
www.SmoothMyPanels.com
I would like to see both light and dark examples. I'm open to any kind of design. I prefer a sleek, modern theme to go along with the logo. Linkora, Ravo, and Clipverse logos can also be added.
Logo and/or web address. Open to all suggestions and ideas. Have fun with it!

```html
<!DOCTYPE html>
<html lang="en">
<head>
<meta charset="utf-8">
<title>Panel Soothe LLC – Business Cards</title>
<link href="https://fonts.googleapis.com/css2?family=Montserrat:wght@400;600;800&family=Roboto:wght@400;500&display=swap" rel="stylesheet">
<style>
  :root{
    --bg:#e9ebee;
    --card-white:#ffffff;
    --card-dark:#1c1c1e;
    --blue:#1f7fe0;
    --blue-deep:#0d3f9e;
    --sky:#37b6f0;
    --grey:#8c8f95;
    --ink:#1a1a1a;
    --muted:#4a4d52;
    --white:#ffffff;
  }
  *{margin:0;padding:0;box-sizing:border-box}
  html,body{width:1200px;height:901px;overflow:hidden;background:var(--bg)}
  .stage{position:relative;width:1200px;height:901px}
  .card{
    position:absolute;top:296px;width:540px;height:309px;
    border-radius:26px;overflow:hidden;
    box-shadow:0 10px 28px rgba(0,0,0,.18);
  }
  .card-front{left:40px;background:var(--card-white)}
  .card-back{left:620px;background:var(--card-dark)}
  .waves{position:absolute;inset:0;width:100%;height:100%}
  .brand{position:absolute;display:flex;align-items:center;gap:8px}
  .brand-dot{width:14px;height:14px;border-radius:50%;background:var(--sky)}
  .brand-name{font-family:"Montserrat",sans-serif;font-weight:800;font-size:25px;letter-spacing:.5px;text-transform:uppercase}
  .tagline{position:absolute;font-family:"Montserrat",sans-serif;font-weight:600;font-size:9.5px;letter-spacing:2px;text-transform:uppercase}
  .card-front .brand{left:32px;top:32px}
  .card-front .brand-name{color:var(--ink)}
  .card-front .tagline{left:54px;top:66px;color:var(--blue)}
  .divider{position:absolute;left:32px;top:84px;width:230px;height:1px;background:#c9ccd1}
  .person{position:absolute;left:32px;top:96px;font-family:"Roboto",sans-serif}
  .person-name{font-size:19px;font-weight:500;letter-spacing:1px;color:var(--ink);text-transform:uppercase}
  .person-role{font-size:11.5px;color:var(--muted);margin-top:3px}
  .contacts{position:absolute;left:300px;top:184px;list-style:none;font-family:"Roboto",sans-serif;font-size:10.5px;color:var(--white)}
  .contacts li{display:flex;align-items:center;gap:8px;height:20px}
  .contacts svg{width:14px;height:14px;flex:none}
  .card-back .brand{left:0;right:0;top:122px;justify-content:center}
  .card-back .brand-name{color:var(--white)}
  .card-back .tagline{left:0;right:0;top:160px;text-align:center;color:var(--sky)}
  .back-rule{position:absolute;left:150px;width:240px;top:180px;height:1px;background:#4b4e54}
</style>
</head>
<body>
<main class="stage">

  <section class="card card-front" aria-label="Business card, front">
    <svg class="waves" viewBox="0 0 540 309" preserveAspectRatio="none" aria-hidden="true">
      <defs>
        <linearGradient id="blueFill" x1="0" y1="0" x2="1" y2="1">
          <stop offset="0" stop-color="#2a8cf0"/>
          <stop offset="1" stop-color="#0d3f9e"/>
        </linearGradient>
      </defs>
      <path d="M0 178 C140 120 300 215 540 128 L540 168 C300 250 150 160 0 222 Z" fill="var(--grey)"/>
      <path d="M0 214 C150 150 300 238 540 158 L540 309 L0 309 Z" fill="url(#blueFill)"/>
      <path d="M0 205 C150 140 300 230 540 150" fill="none" stroke="var(--white)" stroke-width="3"/>
    </svg>

    <div class="brand"><span class="brand-dot"></span><span class="brand-name">Panel Soothe LLC</span></div>
    <div class="tagline">Paintless Dent Removal</div>
    <div class="divider"></div>

    <div class="person">
      <p class="person-name">Mark Fenley</p>
      <p class="person-role">Managing Director</p>
    </div>

    <ul class="contacts">
      <li><svg viewBox="0 0 14 14"><circle cx="7" cy="7" r="7" fill="#fff"/><path d="M4.6 3.6l1.4 1.6-.7 1c.5 1 1.3 1.8 2.3 2.3l1-.7 1.6 1.4-.7 1.2C7 10.3 3.8 7.1 3.4 4.3z" fill="var(--blue-deep)"/></svg>014 582 3907</li>
      <li><svg viewBox="0 0 14 14"><circle cx="7" cy="7" r="7" fill="#fff"/><rect x="5" y="3" width="4" height="8" rx="1" fill="var(--blue-deep)"/></svg>014 582 3907</li>
      <li><svg viewBox="0 0 14 14"><circle cx="7" cy="7" r="7" fill="#fff"/><rect x="3.5" y="4.5" width="7" height="5" fill="none" stroke="var(--blue-deep)"/><path d="M3.5 4.5L7 7.3 10.5 4.5" fill="none" stroke="var(--blue-deep)"/></svg>info@PanelSootheLLC.com</li>
      <li><svg viewBox="0 0 14 14"><circle cx="7" cy="7" r="7" fill="#fff"/><circle cx="7" cy="7" r="3.6" fill="none" stroke="var(--blue-deep)"/><path d="M3.4 7h7.2M7 3.4c-1.8 2-1.8 5.2 0 7.2M7 3.4c1.8 2 1.8 5.2 0 7.2" fill="none" stroke="var(--blue-deep)" stroke-width=".8"/></svg>www.SmoothMyPanels.com</li>
      <li><svg viewBox="0 0 14 14"><circle cx="7" cy="7" r="7" fill="#fff"/><path d="M7 11.2S4.2 8 4.2 6a2.8 2.8 0 015.6 0c0 2-2.8 5.2-2.8 5.2z" fill="var(--blue-deep)"/><circle cx="7" cy="6" r="1" fill="#fff"/></svg>478 Birch Ln Allentown, PA 18117</li>
    </ul>
  </section>

  <section class="card card-back" aria-label="Business card, back">
    <div class="brand"><span class="brand-dot"></span><span class="brand-name">Panel Soothe LLC</span></div>
    <div class="tagline">Paintless Dent Removal</div>
    <div class="back-rule"></div>
  </section>

</main>
</body>
</html>
```